New therapy private practice needs a 2 sided postcard announcing location and services

We need a postcard sized card that is TWO SIDED and shares our new location and services offered. (new location is 3842. W. 58th #2300 in Tulsa, OK 74152) Name of the therapy business is "Bright Path! Counseling". Services offered include individual, marriage, family and group counseling. My phone number to place on the card is (918) 555-0143 and someone can call to schedule a free 20 minute consultation at that number.

These cards will also be mailed in an enclosed envelope or placed in welcome baskets as a marketing tool with possible referral sources like churches, doctors, and lawyers. (That means there does not have to be a space for an address or stamp to mail to. Full use of both sides of the card is important) We would like to see designs that use softer colors such as blue, purples, or greens. The final design should communicate a feeling of peace and hope and a sense of freshness and approachability. Incorporating a tag line such as..... "where you'll find hope!" would be good. My website is www.brightpathnow.example and extra info about my practice is on there. It is important my credentials are listed on the postcard. Lena Marsh Voight, LPC-S, LMFT

I am not looking for a bunch of "box looking pictures". The pictures I am uploading are for ideas, although my logo and picture should be used. I like the type of picture I have on my homepage of my website with the quote "Let your hopes, not your fears shape your future"

Target Market(s)

Primarily women and couples looking for counseling for relationships, anxiety, depression, or life transitions.

Font styles to use
Serif
Script

Colors
3276b5
85acd3
86cfc6
33b8a4
cadf82
876aae
9bcb3c

Requirements
Must have
• My picture, address, website, and phone number as well as my logo.
• Address is: 3842 W. 58th Street #2300 Tulsa, OK 74152
• Web: www.brightpathnow.example
• Email: lena@brightpathnow.example
• Phone: (918) 555-0143
• "Hope anchors the soul" - Heb. 6:19
• On my website, I have a 2 minute video of myself. This may be helpful to watch in getting a "feel" for my counseling practice.
• Services Provided: ANXIETY | DEPRESSION | LIFE TRANSITIONS | MARRIAGE COUNSELING | SEPARATION AND DIVORCE | WOMEN’S ISSUES | ADDICTIONS AND INFIDELITY | PARENT/CHILD RELATIONSHIPS | FAMILY CONFLICT | TRAUMA/GRIEF AND LOSS
Nice to have
• A combination of print and script would be nice. A feeling of tranquility and hope
• I would like to have the statement at the bottom of the card.... " It is my desire for you to discover that no matter the situation you are currently going through….. there’s hope!"
• It would also be nice to have a small area that says: Lena is a graduate of Western Calloway College and has been in private practice for 11 years. She is a regular monthly co-host on the Meadow Broadcast Group at 97.3 FM
Should not have
• Heavy bold or abrasive feel

```html
<!DOCTYPE html>
<html lang="en">
<head>
<meta charset="utf-8">
<title>Bright Path! Counseling – Postcard</title>
<link rel="stylesheet" href="https://fonts.googleapis.com/css2?family=Great+Vibes&family=Roboto+Condensed:wght@300;400;700&display=swap">
<style>
  :root {
    --page-bg: #d9d9d9;
    --cream: #ecf1d3;
    --leaf: #4f8a2f;
    --leaf-dark: #3f7526;
    --ocean: #2f6ea6;
    --ink: #2b2b2b;
    --white: #ffffff;
    --shadow: rgba(0, 0, 0, 0.35);
  }
  * { box-sizing: border-box; margin: 0; padding: 0; }
  html, body { width: 776px; height: 1200px; overflow: hidden; }
  body {
    background: radial-gradient(ellipse at 50% 40%, #f1f1f1 0%, var(--page-bg) 75%);
    font-family: "Roboto Condensed", "Arial Narrow", sans-serif;
    color: var(--ink);
    position: relative;
  }
  .postcard {
    position: absolute;
    left: 78px;
    width: 620px;
    height: 470px;
    overflow: hidden;
    box-shadow: 4px 6px 10px var(--shadow);
  }
  .postcard--front { top: 62px; }
  .postcard--back { top: 586px; background: var(--cream); }

  /* Front */
  .hero-photo {
    position: absolute; inset: 0;
    background:
      radial-gradient(ellipse at 82% 22%, rgba(255, 226, 170, 0.85) 0%, rgba(230, 190, 130, 0.35) 22%, transparent 45%),
      linear-gradient(180deg, #c9cbc4 0%, #8f948c 22%, #5c6453 42%, #343b2b 62%, #2a2418 82%, #5d4c3b 100%);
  }
  .brand {
    position: absolute; left: 48px; top: 36px;
    display: flex; align-items: center; gap: 8px;
    color: var(--white);
    font-size: 20px; font-weight: 400;
  }
  .brand__dot { width: 14px; height: 14px; border-radius: 50%; background: var(--white); }
  .tagline {
    position: absolute; right: 46px; top: 222px;
    color: var(--white);
    text-align: right;
  }
  .tagline__lead { font-size: 27px; font-weight: 700; letter-spacing: 0.3px; }
  .tagline__script {
    font-family: "Great Vibes", cursive;
    font-size: 118px; line-height: 1;
    margin-top: -4px; margin-right: 12px;
  }
  .front-web {
    position: absolute; left: 48px; top: 426px;
    color: var(--white); font-size: 15px; font-weight: 700;
  }

  /* Back */
  .intro { position: absolute; left: 31px; top: 22px; width: 365px; }
  .intro__kicker { font-size: 18px; font-weight: 400; }
  .intro__lead { font-size: 24px; font-weight: 400; margin-top: 4px; }
  .intro__values {
    font-size: 27px; font-weight: 700; color: var(--leaf);
    margin-top: 2px; letter-spacing: 0.2px;
  }
  .intro__values .accent { color: var(--ink); }
  .intro__body {
    font-size: 13px; font-weight: 400; line-height: 21px;
    margin-top: 8px; text-align: justify;
  }
  .counselor { position: absolute; left: 406px; top: 16px; width: 186px; }
  .counselor__photo {
    width: 186px; height: 186px; border-radius: 50%;
    border: 5px solid var(--leaf);
    background: radial-gradient(circle at 50% 40%, #d9c7a0 0%, #b7a36c 40%, #6f7a3c 75%, #4d5a2a 100%);
  }
  .counselor__badge {
    position: absolute; left: 4px; top: 157px; width: 178px; height: 54px;
    background: var(--leaf); color: var(--white);
    border-radius: 6px; text-align: center;
    padding-top: 7px;
  }
  .counselor__name { font-size: 19px; font-weight: 700; }
  .counselor__creds { font-size: 15px; font-weight: 400; margin-top: 1px; }

  .details {
    position: absolute; left: 0; bottom: 0; width: 100%; height: 195px;
    background: var(--ocean); color: var(--white);
  }
  .details__title {
    position: absolute; left: 31px; top: 18px;
    font-size: 26px; font-weight: 700;
  }
  .issues {
    position: absolute; top: 60px; list-style: none;
    font-size: 14.5px; font-weight: 300;
  }
  .issues li { height: 27.5px; padding-left: 14px; position: relative; }
  .issues li::before {
    content: ""; position: absolute; left: 0; top: 7px;
    width: 5px; height: 5px; border-radius: 50%; background: var(--white);
  }
  .issues--first { left: 31px; }
  .issues--second { left: 197px; }
  .contact { position: absolute; left: 398px; top: 38px; width: 215px; }
  .contact__name { font-size: 17px; font-weight: 700; margin-bottom: 10px; }
  .contact__name span { font-weight: 400; }
  .contact__row {
    display: flex; align-items: flex-start; gap: 8px;
    font-size: 14px; font-weight: 400; line-height: 18px; margin-bottom: 5px;
  }
  .contact__row svg { flex: none; width: 13px; height: 13px; margin-top: 2px; }
</style>
</head>
<body>

<section class="postcard postcard--front">
  <div class="hero-photo" role="img" aria-label="Photo of a woman sitting on a rock ledge overlooking a misty forested mountain valley at sunrise"></div>
  <div class="brand"><span class="brand__dot"></span>Bright Path! Counseling</div>
  <div class="tagline">
    <p class="tagline__lead">Where you'll find</p>
    <p class="tagline__script">Hope!</p>
  </div>
  <p class="front-web">www.brightpathnow.example</p>
</section>

<section class="postcard postcard--back">
  <div class="intro">
    <p class="intro__kicker">Today you are one step closer</p>
    <p class="intro__lead">To finding your sense of</p>
    <p class="intro__values">Hope<span class="accent">,</span> <span class="accent">Purpose,</span> &amp; Fulfillment!</p>
    <p class="intro__body">Everyone goes through challenges in life, and while you may have successfully navigated through other difficulties, seeking out the help of a professional can be one of the healthiest decisions you make. Enlisting the help of a professional can provide a fresh perspective on a difficult problem or point you in the direction of a positive solution.</p>
  </div>

  <div class="counselor">
    <div class="counselor__photo" role="img" aria-label="Portrait photo of counselor Lena Marsh Voight"></div>
    <div class="counselor__badge">
      <p class="counselor__name">Lena Marsh Voight</p>
      <p class="counselor__creds">LPC-S, LMFT</p>
    </div>
  </div>

  <div class="details">
    <h2 class="details__title">Issues served</h2>
    <ul class="issues issues--first">
      <li>Anxiety</li>
      <li>Depression</li>
      <li>Life Transitions</li>
      <li>Marriage Counseling</li>
      <li>Separation &amp; Divorce</li>
    </ul>
    <ul class="issues issues--second">
      <li>Women's Issues</li>
      <li>Addictions &amp; Infidelity</li>
      <li>Parent/Child Relationships</li>
      <li>Family Conflict</li>
      <li>Trauma/Grief And Loss</li>
    </ul>
    <div class="contact">
      <p class="contact__name">Bright Path! <span>Counseling</span></p>
      <p class="contact__row">
        <svg viewBox="0 0 16 16" aria-hidden="true"><path fill="#fff" d="M3.6 1.2l2.3 2.9-1.3 1.7c.9 2 2.6 3.7 4.6 4.6l1.7-1.3 2.9 2.3-1.2 2.4C7.5 13.6 2.4 8.5 1.2 2.4z"/></svg>
        (918) 555-0143
      </p>
      <p class="contact__row">
        <svg viewBox="0 0 16 16" aria-hidden="true"><circle cx="8" cy="8" r="6.5" fill="none" stroke="#fff" stroke-width="1.4"/><ellipse cx="8" cy="8" rx="2.8" ry="6.5" fill="none" stroke="#fff" stroke-width="1.2"/><path d="M1.5 8h13" stroke="#fff" stroke-width="1.2"/></svg>
        www.brightpathnow.example
      </p>
      <p class="contact__row">
        <svg viewBox="0 0 16 16" aria-hidden="true"><rect x="1" y="3.5" width="14" height="9" fill="#fff"/><path d="M1 3.5l7 5.5 7-5.5" fill="none" stroke="#2f6ea6" stroke-width="1.3"/></svg>
        lena@brightpathnow.example
      </p>
      <p class="contact__row">
        <svg viewBox="0 0 16 16" aria-hidden="true"><path fill="#fff" d="M8 0.8a5 5 0 0 1 5 5c0 3.8-5 9.6-5 9.6S3 9.6 3 5.8a5 5 0 0 1 5-5z"/><circle cx="8" cy="5.8" r="1.9" fill="#2f6ea6"/></svg>
        <span>3842 W. 58th Street #2300<br>Tulsa, OK 74152</span>
      </p>
    </div>
  </div>
</section>

</body>
</html>
```